Business card

A basic business card using the new logo
The logo has our address on it is all I need is onset with the following

Dale Whitford
Manager of Sales and Service

Cell 508-731-5286

Email dw71846@mailvista.net

Next card

Mark Ellwood
Manager

Cell 978-215-8349

Email mellwood7@qx-post.com

Industry/Entity Type

Business

```html
<!DOCTYPE html>
<html lang="en">
<head>
<meta charset="utf-8">
<title>Business Card – Dale Whitford</title>
<link rel="stylesheet" href="https://fonts.googleapis.com/css2?family=Questrial&family=Cinzel:wght@400;600&display=swap">
<style>
  :root {
    --page-bg: #dcdcdc;
    --card-bg: #f3f3f3;
    --brand-blue: #2f8fce;
    --ink-dark: #3a3a3a;
    --ink-mid: #555555;
    --band-dark: #3b3b3b;
  }
  * { margin: 0; padding: 0; box-sizing: border-box; }
  html, body {
    width: 1200px;
    height: 900px;
    overflow: hidden;
    background: var(--page-bg);
  }
  .canvas {
    position: relative;
    width: 1200px;
    height: 900px;
  }
  .card {
    position: absolute;
    left: 75px;
    top: 150px;
    width: 1050px;
    height: 600px;
    background: var(--card-bg);
    box-shadow: 0 10px 30px rgba(0,0,0,0.18);
    overflow: hidden;
    font-family: "Questrial", Arial, sans-serif;
  }
  .brand {
    position: absolute;
    left: 70px;
    top: 62px;
  }
  .brand-name {
    display: flex;
    align-items: center;
    gap: 14px;
    font-size: 54px;
    color: var(--brand-blue);
    letter-spacing: 1px;
    line-height: 1;
  }
  .brand-dot {
    width: 26px;
    height: 26px;
    border-radius: 50%;
    background: var(--brand-blue);
  }
  .brand-legal {
    margin-top: 10px;
    font-size: 19px;
    color: var(--ink-dark);
  }
  .brand-address {
    margin-top: 4px;
    font-size: 19px;
    color: var(--ink-dark);
  }
  .person {
    position: absolute;
    left: 470px;
    top: 278px;
  }
  .person-name {
    font-family: "Cinzel", Georgia, serif;
    font-weight: 600;
    font-size: 30px;
    letter-spacing: 5px;
    color: var(--ink-dark);
  }
  .person-title {
    margin-top: 8px;
    font-size: 22px;
    letter-spacing: 3px;
    color: var(--brand-blue);
  }
  .contact {
    position: absolute;
    left: 400px;
    top: 382px;
    font-size: 23px;
    letter-spacing: 2.5px;
    color: var(--ink-mid);
    line-height: 1.75;
  }
  .footer-band {
    position: absolute;
    left: 0;
    bottom: 0;
    width: 1050px;
    height: 110px;
  }
</style>
</head>
<body>
  <div class="canvas">
    <section class="card">
      <div class="brand">
        <div class="brand-name"><span class="brand-dot"></span>Northgate</div>
        <div class="brand-legal">Northgate Terminal Services LLC</div>
        <div class="brand-address">52 Linden Rd Harlow MA 01804</div>
      </div>

      <div class="person">
        <div class="person-name">Dale Whitford</div>
        <div class="person-title">Manager of Sales and Service</div>
      </div>

      <div class="contact">
        <div class="contact-phone">508-731-5286</div>
        <div class="contact-email">dw71846@mailvista.net</div>
      </div>

      <svg class="footer-band" viewBox="0 0 1050 110" aria-hidden="true">
        <path d="M340 110 L340 70 Q340 40 380 40 L1050 40 L1050 110 Z" fill="var(--band-dark)"/>
      </svg>
    </section>
  </div>
</body>
</html>
```